Stationary Design to Complement our Website

We would like template designed for word documents that we can use for headed paper. The template should complement the style of our website & incorporate our existing logo. https://www.velmorantravel.com/

The header and footer design should be sperate PNG or JPEG files that we can copy and paste into word header and footers. They should work on A4 & letter sized papers.

Note the main web colours are as follows:

Black
HEX code #2b2c2b
C=71 M=64 Y=64 K=65
RGB 43,44,43

Green
HEX code #116c49
C=88 M=33 Y=82 K=24
RGB 17,108,73

Current fonts are ALEO & Gilroy.

Fonts and colours in new design don't have to match website exactly but should be complementary.

Font styles to use
Serif

Requirements
Must have
• a simple design that complements our website.
Some kind of graphic on the top & some sort of graphic on the bottom. Not just plain logo on top.
designs that incorporate the clouds might look good
Can also incorporate 5* rate harbor rating
Should not have
• no photographs included on the design

```html
<!DOCTYPE html>
<html lang="en">
<head>
<meta charset="utf-8">
<title>Velmoran Travel Letterhead</title>
<link rel="stylesheet" href="https://fonts.googleapis.com/css2?family=Source+Sans+3:wght@400;600&family=Mulish:wght@400&display=swap">
<style>
  :root {
    --backdrop: #e9e9e9;
    --paper: #f6f3f3;
    --ink: #2b2c2b;
    --body-text: #4d4d4f;
    --muted: #555658;
    --green: #116c49;
    --watermark: #e6e8e6;
    --signature-tone: #d9dcdf;
  }
  * { margin: 0; padding: 0; box-sizing: border-box; }
  html, body { width: 1072px; height: 1200px; overflow: hidden; background: var(--backdrop); }
  .letterhead {
    position: absolute; left: 111px; top: 0;
    width: 850px; height: 1200px;
    background: var(--paper);
    overflow: hidden;
    font-family: "Source Sans 3", sans-serif;
    color: var(--body-text);
  }
  .footer-mark {
    position: absolute; left: 330px; top: 700px;
    width: 560px; height: 560px; border-radius: 50%;
    background: var(--watermark);
    z-index: 0;
  }
  .brand { position: absolute; left: 82px; top: 96px; display: flex; align-items: flex-start; gap: 10px; z-index: 1; }
  .brand-dot { width: 26px; height: 26px; border-radius: 50%; background: var(--green); margin-top: 2px; }
  .brand-name {
    font-family: "Source Sans 3", sans-serif; font-weight: 400;
    font-size: 30px; line-height: 38px; letter-spacing: 5px;
    color: var(--ink); text-transform: uppercase; margin-top: 12px;
  }
  .contact { position: absolute; top: 127px; font-family: "Mulish", sans-serif; font-size: 12px; line-height: 15.5px; color: var(--muted); z-index: 1; }
  .contact-address { right: 262px; text-align: right; font-style: normal; }
  .contact-divider { position: absolute; left: 606px; top: 127px; width: 1px; height: 45px; background: var(--green); }
  .contact-lines { left: 622px; }
  .contact-lines li { list-style: none; display: flex; align-items: center; gap: 7px; }
  .contact-lines svg { width: 10px; height: 10px; fill: var(--green); }
  .letter { position: absolute; left: 85px; top: 332px; width: 685px; z-index: 1; }
  .salutation { font-size: 22px; color: var(--muted); margin-bottom: 40px; }
  .letter p.body { font-size: 13.7px; line-height: 20.5px; text-align: justify; hyphens: auto; margin-bottom: 20.5px; }
  .closing { font-size: 13.7px; margin-top: 40px; }
  .signature { width: 110px; height: 45px; margin-top: 22px; background: var(--signature-tone); border-radius: 3px; }
</style>
</head>
<body>
<main class="letterhead">
  <div class="footer-mark" role="img" aria-label="Large faint brand decoration in the lower right corner"></div>
  <header>
    <div class="brand">
      <span class="brand-dot"></span>
      <div class="brand-name">Velmoran<br>Travel</div>
    </div>
    <address class="contact contact-address">
      4120 Larkfield Road<br>
      Brookvale, Oregon 97841<br>
      www.velmorantravel.com
    </address>
    <span class="contact-divider"></span>
    <ul class="contact contact-lines">
      <li><svg viewBox="0 0 10 10"><path d="M2 0.5l2 2-1 1.2c.6 1.3 1.7 2.4 3 3l1.2-1 2 2-1.2 1.8C4.5 9.3.7 5.5.3 1.7z"/></svg>555-284-6130</li>
      <li><svg viewBox="0 0 10 10"><rect x="2.5" y="0.5" width="5" height="3"/><rect x="0.5" y="3.5" width="9" height="4" rx="1"/><rect x="2.5" y="6.5" width="5" height="3"/></svg>555-284-6197</li>
      <li><svg viewBox="0 0 10 10"><path d="M0.5 2h9v6h-9z M0.5 2l4.5 3.5L9.5 2" fill="var(--green)" stroke="var(--paper)" stroke-width="0.8"/></svg>info@velmorantravel.com</li>
    </ul>
  </header>
  <section class="letter" lang="la">
    <p class="salutation" lang="en">Dear Mr. Harlow,</p>
    <p class="body">Lorem ipsum dolor sit amet, consectetur adipiscing elit. Donec orci purus, luctus vitae dignissim eu, iaculis sed purus. Vivamus faucibus, ipsum nec aliquet viverra, leo mauris condimentum ligula, sit amet sagittis enim ligula quis arcu. Nam egestas tortor id nisi porttitor mattis. In tortor ante, ultricies in suscipit a, tempus non massa. Vivamus et auctor mi. Fusce vel massa nulla. Phasellus nec eros mauris, et scelerisque orci.</p>
    <p class="body">Donec malesuada orci vitae nulla accumsan porta a id massa. Quisque accumsan iaculis magna sit amet fringilla. Maecenas consequat, magna eget tincidunt semper, odio nibh rutrum mi, id feugiat ante nisi eu risus. Vestibulum nunc orci, rhoncus a placerat in, ultricies in mi. Cras mattis varius eros, vel fringilla nisi suscipit eget. Quisque scelerisque sagittis nulla at porttitor.</p>
    <p class="body">Sed id augue vitae urna euismod commodo aliquet a quam. Pellentesque arcu velit, cursus et malesuada ut, consequat et diam. Nullam erat sem, rhoncus id ullamcorper vitae, rhoncus et arcu. In ultricies ultricies nulla, ut rutrum nisi iaculis at. Donec eu magna a metus ornare faucibus. Fusce aliquet faucibus ultricies. Morbi semper, est id tincidunt gravida, sem arcu adipiscing lacus, ac bibendum nulla leo eu purus. Quisque nec diam sed risus consectetur a ccumsan quis quis nibh. Vestibulum id purus lorem.</p>
    <p class="body" lang="en">It is a long established fact that a reader will be distracted by the readable content of a page when looking at its layout. The point of using Lorem Ipsum is that it has a more-or-less normal distribution of letters, as opposed to using 'Content here, content here', making it look like readable English. Many desktop publishing packages</p>
    <p class="closing" lang="en">Sincerely,</p>
    <div class="signature" role="img" aria-label="Handwritten signature of the sender"></div>
  </section>
</main>
</body>
</html>
```